Online bill payment portal website design

Online Invoice Payment Website

The customer will click on the logos of the institution they want to pay and the payment will be made at the latest stage to write the customer number.

Invoice payment can be made online. Telephone, Television, Internet, Electricity, Water, Natural Gas, and all institutional payments.

Example website : https://www.selvopay.com/

Industry/Entity Type

Invoice

Logo Text

KolayBorcKapat.Net

Number of Pages Required

4 page

Font styles to use
Serif
Sans Serif

Colors
abd036
33a6d7
876aae
e667a6
ec1f27
f37122
85abd2
0555a3
00a990

Requirements
Must have
• Logos of payment institutions
• Credit Card Payment form
• Customer information form
• COntact page
• List of Institutions
• Accept privacy policies in all forms
Nice to have
• Good and new design :)
Should not have
• Same with selvopay.com ! i want new site

```html
<!DOCTYPE html>
<html lang="tr">
<head>
<meta charset="utf-8">
<title>Anlaşmalı Kurumlar</title>
<link rel="stylesheet" href="https://fonts.googleapis.com/css2?family=Source+Sans+3:wght@400;600;700&display=swap">
<style>
  :root{
    --backdrop:#9e9e9e;
    --page:#ffffff;
    --orange:#f37122;
    --blue:#0555a3;
    --heading-blue:#1c4f9a;
    --cyan:#16a9c9;
    --red:#ec1f27;
    --water:#33a6d7;
    --green:#abd036;
    --teal:#00a990;
    --pink:#e667a6;
    --ink:#1a1a1a;
    --rule:#d9d9d9;
    --field:#f6f6f6;
  }
  *{box-sizing:border-box;margin:0;padding:0}
  html,body{width:1200px;height:1200px;overflow:hidden}
  body{background:var(--backdrop);font-family:"Source Sans 3",sans-serif;color:var(--ink);position:relative}
  .page{position:absolute;left:40px;top:0;width:1120px;height:1117px;background:var(--page);box-shadow:0 3px 6px rgba(0,0,0,.45)}
  .search{position:absolute;left:146px;top:-10px;width:804px;height:40px;display:flex;border:1px solid #e2e2e2;border-top:none}
  .search-input{flex:1;background:var(--field);color:#999;font-size:13px;padding:0 26px;line-height:14px}
  .search-button{width:137px;background:var(--blue);display:flex;justify-content:center;align-items:flex-start;border:none}
  .institutions{position:absolute;left:0;top:94px;width:1120px;height:580px;background:var(--orange);text-align:center}
  .institutions-title{color:#fff;font-weight:700;font-size:25px;line-height:30px;margin-top:59px;letter-spacing:.1px}
  .institution-grid{display:grid;grid-template-columns:repeat(4,150px);column-gap:25px;row-gap:24px;width:675px;margin:37px auto 0;margin-left:221px}
  .institution{display:block;text-decoration:none;color:#fff;font-weight:700;font-size:16px;line-height:20px}
  .institution-tile{width:150px;height:150px;background:#fff;display:flex;align-items:center;justify-content:center;margin-bottom:8px}
  .institution-label{display:block;padding-right:12px}
  .about{position:absolute;left:0;top:718px;width:1120px;text-align:center}
  .about-title{color:var(--heading-blue);font-size:25px;line-height:32px;font-weight:700}
  .about-text{width:760px;margin:8px auto 0;font-size:10.8px;line-height:16px}
  .footer-rule{position:absolute;left:248px;top:910px;width:624px;border-top:1.5px solid var(--rule)}
  .cards{position:absolute;left:466px;top:938px;display:flex;gap:17px}
  .card{width:86px;height:53px;border:1px solid;border-radius:4px;display:flex;align-items:center;justify-content:center;font-weight:700;font-size:16px}
  .card-a{border-color:var(--red);color:var(--red)}
  .card-b{border-color:var(--blue);color:var(--blue)}
  .copyright{position:absolute;left:0;top:1012px;width:1120px;text-align:center;font-size:10.6px}
  .copyright a{color:var(--blue);text-decoration:none}
</style>
</head>
<body>
<div class="page">
  <form class="search">
    <div class="search-input">Kurum ara</div>
    <button class="search-button" type="button" aria-label="Ara">
      <svg width="40" height="30" viewBox="0 0 40 30"><circle cx="18" cy="6" r="11" fill="none" stroke="#fff" stroke-width="3.5"/><line x1="26" y1="14" x2="34" y2="22" stroke="#fff" stroke-width="4" stroke-linecap="round"/></svg>
    </button>
  </form>

  <section class="institutions">
    <h2 class="institutions-title">Fatura ödemesi yapabileceğiniz diğer anlaşmalı kurumlar</h2>
    <div class="institution-grid">
      <a class="institution" href="#"><div class="institution-tile">
        <svg width="58" height="58" viewBox="0 0 58 58" fill="var(--cyan)"><rect x="0" y="0" width="17" height="17"/><rect x="20" y="0" width="17" height="17"/><rect x="40" y="0" width="17" height="17"/><rect x="0" y="20" width="17" height="17"/><rect x="20" y="20" width="17" height="17"/><rect x="40" y="20" width="17" height="17"/><rect x="0" y="40" width="17" height="17"/><rect x="20" y="40" width="17" height="17"/><rect x="40" y="40" width="17" height="17"/></svg>
      </div><span class="institution-label">Tümü</span></a>
      <a class="institution" href="#"><div class="institution-tile">
        <svg width="74" height="74" viewBox="0 0 74 74"><circle cx="37" cy="37" r="34.5" fill="none" stroke="var(--red)" stroke-width="2"/><path d="M42 14 L24 40 H36 L31 60 L51 32 H39 Z" fill="var(--red)"/></svg>
      </div><span class="institution-label">Elektrik</span></a>
      <a class="institution" href="#"><div class="institution-tile">
        <svg width="56" height="80" viewBox="0 0 56 80" fill="none" stroke="var(--orange)" stroke-width="3" stroke-linejoin="round"><path d="M10 4 C22 18 18 28 30 36 C32 28 36 22 36 16 C50 30 56 46 52 62 C48 74 38 78 28 78 C14 78 4 70 3 56 C2 42 10 34 10 4 Z"/><path d="M16 58 L20 46 L26 56 L32 42 L38 54 L42 46 C46 60 40 70 28 70 C20 70 14 66 16 58 Z"/></svg>
      </div><span class="institution-label">Doğalgaz</span></a>
      <a class="institution" href="#"><div class="institution-tile">
        <svg width="50" height="90" viewBox="0 0 50 90"><path d="M25 2 C25 14 46 30 46 48 C46 60 36 70 25 70 C14 70 4 60 4 48 C4 30 25 14 25 2 Z" fill="var(--water)"/><circle cx="25" cy="50" r="8" fill="#fff"/><path d="M2 76 q6 -4 12 0 t12 0 t12 0 t12 0 M2 83 q6 -4 12 0 t12 0 t12 0 t12 0" fill="none" stroke="var(--water)" stroke-width="2.5"/></svg>
      </div><span class="institution-label">Su</span></a>

      <a class="institution" href="#"><div class="institution-tile">
        <svg width="36" height="70" viewBox="0 0 36 70"><rect x="1" y="1" width="34" height="68" rx="5" fill="var(--green)"/><rect x="5" y="9" width="26" height="48" fill="#fff"/><rect x="13" y="4" width="10" height="2" fill="#fff"/><circle cx="18" cy="63" r="3" fill="#fff"/></svg>
      </div><span class="institution-label">Telefon</span></a>
      <a class="institution" href="#"><div class="institution-tile">
        <svg width="80" height="62" viewBox="0 0 80 62" fill="none" stroke="var(--teal)" stroke-width="6" stroke-linecap="round"><path d="M4 18 Q40 -8 76 18"/><path d="M16 30 Q40 12 64 30"/><path d="M28 42 Q40 34 52 42"/><circle cx="40" cy="56" r="4.5" fill="var(--teal)" stroke="none"/></svg>
      </div><span class="institution-label">İnternet</span></a>
      <a class="institution" href="#"><div class="institution-tile">
        <svg width="80" height="56" viewBox="0 0 80 56"><rect x="2" y="2" width="76" height="44" fill="none" stroke="var(--pink)" stroke-width="4"/><rect x="2" y="44" width="76" height="4" fill="var(--pink)"/><path d="M28 48 H52 L56 54 H24 Z" fill="var(--pink)"/></svg>
      </div><span class="institution-label">Televizyon</span></a>
      <a class="institution" href="#"><div class="institution-tile">
        <svg width="72" height="20" viewBox="0 0 72 20" fill="var(--orange)"><circle cx="10" cy="10" r="9.5"/><circle cx="36" cy="10" r="9.5"/><circle cx="62" cy="10" r="9.5"/></svg>
      </div><span class="institution-label">Diğer</span></a>
    </div>
  </section>

  <section class="about">
    <h2 class="about-title">Sedper doro</h2>
    <p class="about-text">Sed ut perspiciatis unde omnis iste natus error sit voluptatem accusantium doloremque laudantium, totam rem aperiam, eaque ipsa quae ab illo inventore veritatis et quasi architecto beatae vitae dicta sunt explicabo. Nemo enim ipsam voluptatem quia voluptas sit aspernatur aut odit aut fugit, sed quia consequuntur magni dolores eos qui ratione voluptatem sequi nesciunt. Neque porro quisquam est, qui dolorem ipsum quia dolor sit amet, consectetur, adipisci velit, sed quia non numquam eius modi tempora incidunt ut labore et dolore magnam aliquam quaerat voluptatem. Ut enim ad minima veniam, quis nostrum exercitationem ullam corporis suscipit laboriosam, nisi ut aliquid ex ea commodi consequatur? Quis autem vel eum iure reprehenderit qui in ea voluptate velit esse quam nihil molestiae consequatur, vel illum qui dolorem eum fugiat quo voluptas nulla pariatu</p>
  </section>

  <div class="footer-rule"></div>
  <div class="cards">
    <div class="card card-a">Kartix</div>
    <div class="card card-b">Payora</div>
  </div>
  <p class="copyright">© 2017 Companyname. <a href="#">Privacy policies</a></p>
</div>
</body>
</html>
```